Ridgeline Crude Advisors needs a logo design and business card layout.

RIDGELINE is a consulting firm in oil and gas, specializing in upstream engineering and field work. We provide engineering solutions for the complete wellbore cycle from casing design to flowback. This includes completion and production design. On-site job supervision and project engineering for conventional and unconventional reservoirs. Asset analysis by reviewing operational conditions of asset packages to determine value of potential acquisitions or divesture.

```html
<!DOCTYPE html>
<html lang="en">
<head>
<meta charset="utf-8">
<title>Ridgeline Crude Advisors – Business Card</title>
<link href="https://fonts.googleapis.com/css2?family=Arimo:wght@400&family=Lato:wght@400;900&display=swap" rel="stylesheet">
<style>
  :root {
    --backdrop: #2b2b2b;
    --card: #1e1e1e;
    --brand-red: #e8222b;
    --brand-blue: #1a62a8;
    --ink-light: #f2f2f2;
    --divider: #d9d9d9;
  }
  * { box-sizing: border-box; margin: 0; padding: 0; }
  html, body {
    width: 1200px; height: 900px; overflow: hidden;
    background: var(--backdrop);
    font-family: "Lato", sans-serif;
  }
  .canvas { position: relative; width: 1200px; height: 900px; }
  .card {
    position: absolute; left: 280px;
    width: 640px; height: 366px;
    background: var(--card);
    border-bottom: 5px solid var(--brand-blue);
    box-shadow: 0 10px 30px rgba(0,0,0,.45);
  }
  .card--front { top: 62px; }
  .card--back  { top: 472px; }

  .wordmark {
    color: var(--brand-red);
    font-family: "Lato", sans-serif;
    font-weight: 900;
    text-align: center;
    line-height: 1;
    text-transform: uppercase;
  }
  .wordmark__main { display: block; font-size: 72px; letter-spacing: 3px; }
  .wordmark__sub {
    display: block; font-size: 17px; letter-spacing: 6px; margin-top: 8px;
  }
  .card--front .wordmark {
    position: absolute; left: 0; right: 0; top: 128px;
  }
  .card--back .wordmark {
    position: absolute; left: 24px; width: 304px; top: 142px;
  }
  .card--back .wordmark__main { font-size: 44px; letter-spacing: 2px; }
  .card--back .wordmark__sub { font-size: 12px; letter-spacing: 4px; margin-top: 6px; }

  .divider {
    position: absolute; left: 350px; top: 90px;
    width: 2px; height: 180px; background: var(--divider);
  }
  .contact {
    position: absolute; left: 378px; top: 86px; width: 250px;
    color: var(--ink-light);
  }
  .contact__name {
    font-family: "Arimo", sans-serif;
    color: var(--brand-blue); font-size: 27px;
    text-transform: uppercase; letter-spacing: .5px; line-height: 1;
    white-space: nowrap;
  }
  .contact__title { font-size: 15px; margin-top: 4px; }
  .contact__address { font-size: 15px; line-height: 1.35; margin-top: 16px; }
  .contact__list { list-style: none; margin-top: 8px; }
  .contact__item {
    display: flex; align-items: center; gap: 8px;
    font-size: 15px; line-height: 1.5;
  }
  .contact__icon { width: 10px; height: 10px; flex: none; }
</style>
</head>
<body>
<main class="canvas">

  <section class="card card--front" aria-label="Card front">
    <div class="wordmark">
      <span class="wordmark__main">Ridgeline</span>
      <span class="wordmark__sub">Crude Advisors</span>
    </div>
  </section>

  <section class="card card--back" aria-label="Card back">
    <div class="wordmark">
      <span class="wordmark__main">Ridgeline</span>
      <span class="wordmark__sub">Crude Advisors</span>
    </div>

    <div class="divider"></div>

    <div class="contact">
      <p class="contact__name">Dana Whitlock</p>
      <p class="contact__title">Director</p>
      <p class="contact__address">4410 W. Mesa Ridge Dr.<br>#212 Tempe, AZ 85282</p>
      <ul class="contact__list">
        <li class="contact__item">
          <svg class="contact__icon" viewBox="0 0 10 10" aria-hidden="true"><path d="M2 0.5 L3.6 2.6 L2.6 3.6 Q3.6 6 6.4 7.4 L7.4 6.4 L9.5 8 L8.2 9.5 Q1 8 0.5 1.8 Z" fill="var(--brand-blue)"/></svg>
          (480) 555-0147
        </li>
        <li class="contact__item">
          <svg class="contact__icon" viewBox="0 0 10 10" aria-hidden="true"><rect x="0.5" y="1.8" width="9" height="6.4" fill="none" stroke="var(--brand-blue)"/><path d="M0.5 1.8 L5 5.4 L9.5 1.8" fill="none" stroke="var(--brand-blue)"/></svg>
          info@ridgelinecrude.com
        </li>
        <li class="contact__item">
          <svg class="contact__icon" viewBox="0 0 10 10" aria-hidden="true"><circle cx="5" cy="5" r="4.5" fill="none" stroke="var(--brand-blue)"/><ellipse cx="5" cy="5" rx="2" ry="4.5" fill="none" stroke="var(--brand-blue)"/><path d="M0.5 5 H9.5" stroke="var(--brand-blue)"/></svg>
          www.ridgelinecrude.com
        </li>
      </ul>
    </div>
  </section>

</main>
</body>
</html>
```